Boat Dealership Needs A Post Boat Show Sale Flyer - 8.5X11

We need an 8.5X11 flyer to hand out at our boat show to promote a sale at our dealership following our boat show.

Annual Post Boat Show Open House

February 25 - March 5
Extended Hours
Friday, February 25 - 9 AM to 6 PM
Saturday, February 26 -9 AM to 6 PM
Sunday, February 27 - 11 AM to 3 PM
Monday, February 28 through Friday, March 4 - 9 AM to 6 PM
Saturday, March 5 - 9 AM to 3 PM
After hours by appointment

Phone - (555) 418-3627
Website – harbeldmarine.example

Didn't buy at the show? Wondering what to do after the show?
Don't miss your last chance to secure boat show season pricing.
Our three large, indoor showrooms are fully stocked, and our discounted boat show pricing continues.
Extended hours and continued show pricing.
In-stock incentives and special financing.
New pontoons in-stock starting at $25,995 and less than $150 a month with approved credit.
New tritoons in stock starting at $38,995 and less than $250 a month with approved credit.
Side console Talvin Hulls fishing boats starting at $17,995 and less than $125 a month with approved credit.
Special pricing on remaining in-stock Vorlanes.
Save thousands on Delsmoor.

Family-owned relaxed atmosphere.
Refreshments provided.
Prefer to shop virtually? Shop 24/7 on our website at harbeldmarine.example or set up a real-time video call.

Proudly Offering – Harbeld, Ketrin, Ondaway, and Drayloft Pontoons, Vorlane, Quilto, Delsmoor, Talvin Hulls

We would like our brand logos on the design.

Follow Us On Plazaly, Snapverse, and Vidloop

Colors
FFF300
FFF600
FEFA6F
FFFEC7
FFFEE8
FFC000
F8CF3A
FAE287
FDF2CF
FEFAEE
F0912C
F2A743
F7CA91
FBE8D2
FDF5EE
EE7325
F08F49
F5BC92
FAE3D3
FDF4ED
EB3D1F
EC4F4E
F09395
F8D3D4
FCEDEE

```html
<!DOCTYPE html>
<html lang="en">
<head>
<meta charset="utf-8">
<title>Harbeld Boating – Annual Post Boat Show Open House</title>
<link href="https://fonts.googleapis.com/css2?family=Red+Hat+Display:wght@400;500;600;700;800&display=swap" rel="stylesheet">
<style>
:root{
  --backdrop:#bdbdbd;
  --orange:#ee7325;
  --orange-light:#f0912c;
  --red:#eb3d1f;
  --gold:#ffc000;
  --gold-soft:#f8cf3a;
  --ink:#232323;
  --wave-edge:#8c8c8c;
  --white:#ffffff;
  --sky:#e9f1f7;
  --sea:#a9c3d6;
}
*{margin:0;padding:0;box-sizing:border-box}
html,body{width:1200px;height:1117px;overflow:hidden}
body{background:var(--backdrop);font-family:"Red Hat Display",Arial,sans-serif;color:var(--ink);position:relative}
.page{position:absolute;top:196px;width:513px;height:725px;background:var(--white);overflow:hidden}
.page--front{left:74px}
.page--back{left:613px}
.abs{position:absolute}
.sea-scene{position:absolute;left:0;right:0;top:223px;bottom:0;background:linear-gradient(180deg,#ffffff 0%,var(--sky) 55%,var(--sea) 100%)}
.page--back .sea-scene{top:520px;background:linear-gradient(180deg,#ffffff 0%,var(--sky) 40%,var(--sea) 100%)}
.band{position:absolute;left:0;background:linear-gradient(90deg,var(--orange) 0%,var(--red) 100%)}
/* logo */
.brand{position:absolute;left:40px;top:30px;display:flex;align-items:center;gap:10px}
.brand__dot{width:44px;height:44px;border-radius:50%;background:var(--orange)}
.brand__name{font-weight:800;font-size:20px;letter-spacing:2px;color:var(--red);line-height:1}
/* front title */
.title{position:absolute;left:46px;top:112px;color:var(--white);font-weight:700;line-height:1}
.title__small{font-size:28px;display:block}
.title__big{font-size:42px;display:block;margin:3px 0 2px;letter-spacing:-.5px}
.brush{position:absolute;background:var(--ink);color:var(--white);font-weight:700;display:flex;align-items:center;justify-content:center;clip-path:polygon(0 35%,12% 18%,45% 8%,80% 0,100% 22%,92% 45%,100% 70%,70% 85%,30% 100%,6% 80%,10% 60%)}
.dates{left:19px;top:244px;width:350px;height:46px;font-size:19px}
.extended{position:absolute;left:75px;top:294px;width:237px;display:flex;align-items:center;gap:12px;font-size:19px;font-weight:600}
.extended::before,.extended::after{content:"";flex:1;height:2px;background:var(--ink)}
.slot{position:absolute;display:flex;gap:8px;font-size:13.2px;line-height:1.35;color:#333}
.slot b{font-weight:700}
.slot svg{flex:none;margin-top:3px}
.divider{position:absolute;left:191px;top:340px;height:75px;border-left:1.5px dashed var(--orange)}
.pill{position:absolute;background:linear-gradient(180deg,var(--gold-soft),#e7a91e);border-radius:10px;color:var(--white);font-weight:700;text-align:center}
.tag{position:absolute;background:var(--red);border:2px solid var(--white);border-radius:5px;color:var(--white);text-align:center}
.front-pill{left:65px;top:444px;width:257px;height:36px;font-size:13.5px;padding-top:6px}
.front-tag{left:101px;top:469px;width:186px;height:23px;font-size:12px;line-height:19px}
.photo-people{position:absolute;right:0;top:270px;width:160px;height:330px;background:linear-gradient(180deg,#d9c5b4,#6d8fab 70%,#c9d6e0);border-radius:80px 0 0 0;opacity:.9}
/* footer */
.footer{position:absolute;left:0;bottom:0;width:513px;height:135px}
.contact-phone{position:absolute;left:195px;top:642px;display:flex;align-items:center;gap:9px;color:var(--white);font-weight:600;font-size:30px}
.contact-web{position:absolute;left:192px;top:680px;color:var(--white);font-size:18px;font-weight:500}
/* back */
.heading{position:absolute;left:40px;top:36px;font-weight:700;font-size:19.5px;line-height:1.03;text-transform:uppercase}
.heading span{color:var(--red);font-weight:500;display:block}
.lead{position:absolute;left:40px;top:121px;color:var(--white);font-size:12.5px;line-height:1.2}
.offers{position:absolute;left:40px;top:193px;width:355px;list-style:none}
.offers li{position:absolute;left:0;display:flex;gap:7px;font-size:9.4px;line-height:1.15;color:#333;width:100%}
.offers li svg{flex:none;margin-top:1px}
.offering{left:125px;top:410px;width:265px;height:38px;font-size:16px}
.brands-list{position:absolute;left:70px;top:455px;width:372px;text-align:center;font-size:10.5px;line-height:1.35;color:#333;font-weight:500}
.back-pill{left:51px;top:488px;width:411px;height:48px;font-size:20px;padding-top:7px}
.back-tag{left:131px;top:523px;width:249px;height:29px;font-size:15.5px;font-weight:700;line-height:25px}
.virtual{position:absolute;left:40px;top:562px;width:433px;text-align:center;font-size:10.2px;font-weight:600;line-height:1.4;color:var(--ink)}
.virtual em{font-style:normal;color:var(--red)}
.back-contact{position:absolute;left:65px;top:652px;display:flex;align-items:center;gap:12px;color:var(--white);font-size:18px;font-weight:500}
.back-contact .sep{width:1px;height:18px;border-left:1.5px dashed var(--gold)}
.back-contact span{display:flex;align-items:center;gap:7px}
.follow{position:absolute;left:0;width:513px;top:686px;text-align:center;color:#d6d6d6;font-size:9.6px;font-weight:500}
</style>
</head>
<body>

<!-- FRONT -->
<section class="page page--front">
  <div class="sea-scene" role="img" aria-label="Photo of a lake with a boat at the shoreline"></div>
  <div class="photo-people" role="img" aria-label="Photo of a young man jumping off a boat while a woman cheers"></div>

  <div class="brand">
    <div class="brand__dot"></div>
    <div class="brand__name">HARBELD BOATING</div>
  </div>

  <div class="band" style="top:97px;height:126px;width:513px"></div>

  <svg class="abs" style="left:250px;top:-30px" width="280" height="290" viewBox="0 0 280 290">
    <defs><linearGradient id="ringF" x1="0" y1="0" x2="0" y2="1"><stop offset="0" stop-color="#f2a743"/><stop offset="1" stop-color="#eb3d1f"/></linearGradient>
    <linearGradient id="photoF" x1="0" y1="0" x2="0" y2="1"><stop offset="0" stop-color="#cfe0ef"/><stop offset=".5" stop-color="#7e9db8"/><stop offset="1" stop-color="#3f5c74"/></linearGradient></defs>
    <circle cx="180" cy="142" r="128" fill="url(#ringF)"/>
    <circle cx="180" cy="142" r="112" fill="#fff"/>
    <circle cx="180" cy="142" r="102" fill="url(#photoF)" role="img" aria-label="Photo of a wakesurfer riding behind a red and white boat"/>
  </svg>

  <h1 class="title">
    <span class="title__small">ANNUAL POST</span>
    <span class="title__big">BOAT SHOW</span>
    <span class="title__small">OPEN HOUSE</span>
  </h1>

  <div class="brush dates">February 25 - March 5</div>
  <div class="extended">Extended Hours</div>

  <div class="slot" style="left:37px;top:336px"><svg width="22" height="22" viewBox="0 0 22 22"><circle cx="11" cy="11" r="9" fill="none" stroke="#eb3d1f" stroke-width="2.4"/><path d="M6 11l4 4 8-10" fill="none" stroke="#eb3d1f" stroke-width="2.6" stroke-linecap="round"/></svg><div><b>Friday</b>, February<br>25 - 9 AM to 6 PM</div></div>
  <div class="slot" style="left:204px;top:334px"><svg width="22" height="22" viewBox="0 0 22 22"><circle cx="11" cy="11" r="9" fill="none" stroke="#eb3d1f" stroke-width="2.4"/><path d="M6 11l4 4 8-10" fill="none" stroke="#eb3d1f" stroke-width="2.6" stroke-linecap="round"/></svg><div><b>Saturday,</b> February<br>26 -9 AM to 6 PM</div></div>
  <div class="slot" style="left:37px;top:389px"><svg width="22" height="22" viewBox="0 0 22 22"><circle cx="11" cy="11" r="9" fill="none" stroke="#eb3d1f" stroke-width="2.4"/><path d="M6 11l4 4 8-10" fill="none" stroke="#eb3d1f" stroke-width="2.6" stroke-linecap="round"/></svg><div><b>Sunday,</b> February<br>27 - 11 AM to 3 PM</div></div>
  <div class="slot" style="left:204px;top:381px"><svg width="22" height="22" viewBox="0 0 22 22"><circle cx="11" cy="11" r="9" fill="none" stroke="#eb3d1f" stroke-width="2.4"/><path d="M6 11l4 4 8-10" fill="none" stroke="#eb3d1f" stroke-width="2.6" stroke-linecap="round"/></svg><div><b>Monday,</b> February 28<br>through <b>Friday,</b> March<br>4 - 9 AM =to 6 PM</div></div>
  <div class="divider"></div>

  <div class="pill front-pill">Saturday, March 5 - 9 AM to 3 PM</div>
  <div class="tag front-tag">After hours by appointment</div>

  <svg class="footer" viewBox="0 0 513 135" preserveAspectRatio="none">
    <path d="M0 60 C60 0 120 10 180 45 C240 80 300 20 370 20 C430 20 470 40 513 30 L513 135 L0 135Z" fill="#8c8c8c"/>
    <path d="M0 68 C60 12 120 20 180 55 C240 90 300 32 370 32 C430 32 470 50 513 40 L513 135 L0 135Z" fill="#232323"/>
  </svg>
  <div class="contact-phone">
    <svg width="28" height="28" viewBox="0 0 28 28"><circle cx="14" cy="14" r="14" fill="#f8cf3a"/><path d="M9 7l3 0 1.5 4-2 1.5c1 2 2.5 3.5 4.5 4.5l1.5-2 4 1.5v3c0 1-1 2-2 2C13 21 7 15 7 9c0-1 1-2 2-2z" fill="#232323"/></svg>
    (555) 418-3627
  </div>
  <div class="contact-web">harbeldmarine.example</div>
</section>

<!-- BACK -->
<section class="page page--back">
  <div class="sea-scene" role="img" aria-label="Photo of a calm lake with a distant tree line"></div>

  <h2 class="heading"><span>Didn't buy at the show?</span>Wondering what to do<br>after the show?</h2>

  <div class="band" style="top:110px;height:55px;width:330px"></div>
  <p class="lead">Don't miss your last chance to secure<br>boat show season pricing.</p>

  <svg class="abs" style="left:295px;top:-40px" width="218" height="290" viewBox="0 0 218 290">
    <defs><linearGradient id="ringB" x1="0" y1="0" x2="0" y2="1"><stop offset="0" stop-color="#f2a743"/><stop offset="1" stop-color="#ee7325"/></linearGradient>
    <linearGradient id="photoB1" x1="0" y1="0" x2="0" y2="1"><stop offset="0" stop-color="#7f9a6c"/><stop offset=".6" stop-color="#b9b29a"/><stop offset="1" stop-color="#e6e6e6"/></linearGradient></defs>
    <circle cx="128" cy="110" r="118" fill="url(#ringB)"/>
    <circle cx="128" cy="110" r="103" fill="#fff"/>
    <circle cx="128" cy="110" r="94" fill="url(#photoB1)" role="img" aria-label="Photo of a couple walking off a pontoon boat onto a grassy shore"/>
  </svg>
  <svg class="abs" style="left:375px;top:165px" width="138" height="175" viewBox="0 0 138 175">
    <defs><linearGradient id="photoB2" x1="0" y1="0" x2="0" y2="1"><stop offset="0" stop-color="#dfe8ef"/><stop offset=".55" stop-color="#5c6670"/><stop offset="1" stop-color="#2d3a44"/></linearGradient></defs>
    <circle cx="85" cy="88" r="82" fill="url(#ringB)"/>
    <circle cx="85" cy="88" r="70" fill="#fff"/>
    <circle cx="85" cy="88" r="63" fill="url(#photoB2)" role="img" aria-label="Photo of friends cruising on a pontoon boat"/>
  </svg>

  <ul class="offers">
    <li style="top:0;width:315px"><svg width="10" height="10" viewBox="0 0 22 22"><circle cx="11" cy="11" r="9" fill="none" stroke="#eb3d1f" stroke-width="3"/><path d="M6 11l4 4 8-10" fill="none" stroke="#eb3d1f" stroke-width="3"/></svg><span>Our three large, indoor showrooms are fully stocked, and our discounted boat show pricing continues.</span></li>
    <li style="top:32px"><svg width="10" height="10" viewBox="0 0 22 22"><circle cx="11" cy="11" r="9" fill="none" stroke="#eb3d1f" stroke-width="3"/><path d="M6 11l4 4 8-10" fill="none" stroke="#eb3d1f" stroke-width="3"/></svg><span>Extended hours and continued show pricing.</span></li>
    <li style="top:53px"><svg width="10" height="10" viewBox="0 0 22 22"><circle cx="11" cy="11" r="9" fill="none" stroke="#eb3d1f" stroke-width="3"/><path d="M6 11l4 4 8-10" fill="none" stroke="#eb3d1f" stroke-width="3"/></svg><span>In-stock incentives and special financing.</span></li>
    <li style="top:75px;width:335px"><svg width="10" height="10" viewBox="0 0 22 22"><circle cx="11" cy="11" r="9" fill="none" stroke="#eb3d1f" stroke-width="3"/><path d="M6 11l4 4 8-10" fill="none" stroke="#eb3d1f" stroke-width="3"/></svg><span>New pontoons in-stock starting at $25,995 and less than $150 a month with approved credit.</span></li>
    <li style="top:107px;width:335px"><svg width="10" height="10" viewBox="0 0 22 22"><circle cx="11" cy="11" r="9" fill="none" stroke="#eb3d1f" stroke-width="3"/><path d="M6 11l4 4 8-10" fill="none" stroke="#eb3d1f" stroke-width="3"/></svg><span>New tritoons in stock starting at $38,995 and less than $250 a month with approved credit.</span></li>
    <li style="top:139px;width:385px"><svg width="10" height="10" viewBox="0 0 22 22"><circle cx="11" cy="11" r="9" fill="none" stroke="#eb3d1f" stroke-width="3"/><path d="M6 11l4 4 8-10" fill="none" stroke="#eb3d1f" stroke-width="3"/></svg><span>Side console Talvin Hulls fishing boats starting at $17,995 and less than $125 a month with approved credit.</span></li>
    <li style="top:171px"><svg width="10" height="10" viewBox="0 0 22 22"><circle cx="11" cy="11" r="9" fill="none" stroke="#eb3d1f" stroke-width="3"/><path d="M6 11l4 4 8-10" fill="none" stroke="#eb3d1f" stroke-width="3"/></svg><span>Special pricing on remaining in-stock Vorlanes.</span></li>
    <li style="top:192px"><svg width="10" height="10" viewBox="0 0 22 22"><circle cx="11" cy="11" r="9" fill="none" stroke="#eb3d1f" stroke-width="3"/><path d="M6 11l4 4 8-10" fill="none" stroke="#eb3d1f" stroke-width="3"/></svg><span>Save thousands on Delsmoor.</span></li>
  </ul>

  <div class="brush offering">Proudly Offering</div>
  <p class="brands-list">Harbeld, Ketrin, Ondaway, and Drayloft Pontoons, Vorlane, Quilto,<br>Delsmoor, Talvin Hulls</p>

  <div class="pill back-pill">Family-owned relaxed atmosphere</div>
  <div class="tag back-tag">Refreshments provided.</div>

  <p class="virtual"><em>Prefer to shop virtually?</em> Shop 24/7 on our website at harbeldmarine.example<br>or set up a real-time video call.</p>

  <svg class="footer" viewBox="0 0 513 135" preserveAspectRatio="none" style="height:150px">
    <path d="M0 25 C30 5 60 0 100 30 C150 65 200 65 260 40 C320 15 380 40 430 35 C470 30 495 25 513 10 L513 150 L0 150Z" fill="#8c8c8c"/>
    <path d="M0 38 C30 18 60 14 100 42 C150 78 200 78 260 52 C320 28 380 52 430 47 C470 43 495 38 513 24 L513 150 L0 150Z" fill="#232323"/>
  </svg>
  <div class="back-contact">
    <span><svg width="15" height="15" viewBox="0 0 28 28"><circle cx="14" cy="14" r="14" fill="#f8cf3a"/><path d="M9 7l3 0 1.5 4-2 1.5c1 2 2.5 3.5 4.5 4.5l1.5-2 4 1.5v3c0 1-1 2-2 2C13 21 7 15 7 9c0-1 1-2 2-2z" fill="#232323"/></svg>(555) 418-3627</span>
    <i class="sep"></i>
    <span><svg width="15" height="15" viewBox="0 0 20 20" fill="none" stroke="#f8cf3a" stroke-width="1.5"><circle cx="10" cy="10" r="8.5"/><ellipse cx="10" cy="10" rx="3.8" ry="8.5"/><path d="M1.5 10h17M3 5.5h14M3 14.5h14"/></svg>harbeldmarine.example</span>
  </div>
  <p class="follow">Follow Us On Plazaly, Snapverse, and Vidloop.</p>
</section>

</body>
</html>
```